Brindle Advisory Business Card Design

Business card for business consulting company, using attached logo. We do financial and strategic consulting, and want a clean, professional image with a bit of fun. Our logo is a flat whale tail, which symbolizes the Orca whale, a highly collaborative, group based animal that is very successful in navigating the ocean, protecting the herd, and hunting. We like the logo that is blue and gray on white one one side, but would be open to a blue card with white lettering on the other side... or whatever you'd suggest
Updates
Hi all - I have had the logo modified to take the shadowing off the tail. I will post it on the brief... under a file name called updated logo. thank you Added Saturday, April 25, 2015
Target Market(s)
Small to medium sized businesses ($10M to $500M in revenue per year), financial and sales executives, general managers, attorneys and CPAs
Industry/Entity Type
Financial
Contact Information for Business Card
Want company name, contact info - name, title, telephone, email, website, linkedin, twitter and Facebook. No physical address yet.
Requirements
Must have
- contemporary design, bold, strong, confident but with a bit of fun. prominently feature the logo and the whale tail icon
Nice to have
- unique touches that would differentiate us from a regular card... for example, logo and writing all on front on white background, but on back - logo in white on a blue background
- open to idea of different shapes of card than standard... but not sure
Should not have
- ?

```html
<!DOCTYPE html>
<html lang="en">
<head>
<meta charset="utf-8">
<title>Brindle Advisory Business Cards</title>
<link href="https://fonts.googleapis.com/css2?family=Open+Sans:wght@400;600;700&display=swap" rel="stylesheet">
<style>
  :root {
    --page: #f1eee8;
    --card: #1b365f;
    --white: #ffffff;
    --muted: #c7c9cd;
  }
  * { margin: 0; padding: 0; box-sizing: border-box; }
  html, body { width: 1189px; height: 1200px; overflow: hidden; }
  body { background: var(--page); font-family: "Open Sans", Arial, sans-serif; position: relative; }

  .card {
    position: absolute; left: 172px; width: 855px; height: 486px;
    background: var(--card); border-radius: 18px; color: var(--white);
  }
  .card--front { top: 69px; }
  .card--back { top: 628px; }

  .mark-square { position: absolute; background: var(--white); border-radius: 10px; }

  .wordmark { position: absolute; font-weight: 600; white-space: nowrap; line-height: 1; color: var(--white); }
  .tagline { position: absolute; font-size: 17px; white-space: nowrap; color: var(--white); line-height: 1; }

  /* front */
  .card--front .mark-square { left: 132px; top: 193px; width: 98px; height: 99px; }
  .card--front .wordmark { left: 240px; top: 210px; font-size: 70px; letter-spacing: -2px; }
  .card--front .tagline { right: 130px; top: 288px; }

  .web-row { position: absolute; left: 132px; width: 595px; top: 368px; display: flex; align-items: center; gap: 18px; }
  .web-row .rule { flex: 1; height: 2px; background: var(--white); border-radius: 2px; }
  .web-row .rule--left { background: linear-gradient(to right, rgba(255,255,255,0.2), var(--white)); }
  .web-row .rule--right { background: linear-gradient(to left, rgba(255,255,255,0.2), var(--white)); }
  .website { font-weight: 700; font-size: 29px; letter-spacing: 0.3px; }

  /* back */
  .card--back .mark-square { left: 158px; top: 151px; width: 101px; height: 100px; }
  .card--back .wordmark { left: 40px; width: 340px; text-align: center; top: 278px; font-size: 42px; letter-spacing: -1.5px; }
  .card--back .tagline { right: 475px; top: 327px; font-size: 14px; }

  .divider { position: absolute; left: 420px; top: 71px; width: 2px; height: 339px; background: var(--white); opacity: 0.85; }

  .person { position: absolute; left: 454px; top: 82px; }
  .person-name { font-weight: 700; font-size: 36px; line-height: 40px; }
  .person-title { font-weight: 600; font-size: 26px; line-height: 28px; color: var(--muted); margin-left: 3px; letter-spacing: 0.5px; }

  .address { position: absolute; left: 456px; top: 180px; font-weight: 600; font-size: 24px; line-height: 33px; color: var(--muted); letter-spacing: 0.3px; }

  .contacts { position: absolute; left: 458px; top: 259px; list-style: none; }
  .contacts li { display: flex; align-items: center; height: 28.5px; font-weight: 600; font-size: 24px; color: var(--muted); letter-spacing: 0.3px; }
  .contacts .icon { width: 24px; height: 24px; margin-right: 14px; flex: none; }
  .contacts .icon--plain { background: var(--white); border-radius: 4px; }
</style>
</head>
<body>

<section class="card card--front">
  <div class="mark-square"></div>
  <div class="wordmark">brindleadvisory</div>
  <div class="tagline">business consulting</div>
  <div class="web-row">
    <span class="rule rule--left"></span>
    <span class="website">www.brindlellc.com</span>
    <span class="rule rule--right"></span>
  </div>
</section>

<section class="card card--back">
  <div class="mark-square"></div>
  <div class="wordmark">brindleadvisory</div>
  <div class="tagline">business consulting</div>

  <div class="divider"></div>

  <div class="person">
    <div class="person-name">Daniel Hartwell</div>
    <div class="person-title">Managing Director</div>
  </div>

  <div class="address">1840 Larkmoor Fenwick<br>MI 49020 US</div>

  <ul class="contacts">
    <li>
      <svg class="icon" viewBox="0 0 24 24" aria-hidden="true">
        <rect width="24" height="24" rx="4" fill="#fff"/>
        <path d="M8 4.5c1 0 2.2 2.6 2.2 3.4 0 .9-1.3 1.2-1.3 2 0 1.5 2.2 5 3.6 5.6.8.3 1.4-1 2.2-.8.8.2 2.6 2.6 2.4 3.4-.3 1-2 1.7-3 1.5C10 18.9 5.5 12 5.8 7.6 5.9 6 6.8 4.5 8 4.5z" fill="#1b365f"/>
      </svg>
      +1.555.014.2290
    </li>
    <li>
      <svg class="icon" viewBox="0 0 24 24" aria-hidden="true">
        <rect width="24" height="24" rx="4" fill="#fff"/>
        <rect x="4" y="6.5" width="16" height="11" fill="none" stroke="#1b365f" stroke-width="1.6"/>
        <path d="M4 6.5l8 6.5 8-6.5M4 17.5l6-5.5M20 17.5l-6-5.5" fill="none" stroke="#1b365f" stroke-width="1.6"/>
      </svg>
      dhartwell@brindlellc.com
    </li>
    <li><span class="icon icon--plain"></span>brindleadvisory</li>
    <li><span class="icon icon--plain"></span>@brindleadvisory</li>
    <li><span class="icon icon--plain"></span>brindleadvisory</li>
  </ul>
</section>

</body>
</html>
```